Wedding Guestbook/Questionnaire Pages

I am looking for questionnaire-style guest book pages for a friend's wedding. The bride wants her guests to fill out a page of reflections on the couple and the wedding in lieu of a traditional guest book. The pages would be printed on 12x12 paper and bound in a book after the wedding.

I've attached a photo of the style of the pages as well as several documents that show colors and give a feel for the wedding.

I understand that this isn't a common project so I welcome any questions and would be more than happy to clarify things.

Thank you!

Target Market(s)

The bride and groom are a young couple and the wedding is more fun and whimisical than formal. The colors are primarily purple with green and silver accents.

Industry/Entity Type

Wedding

Requirements
Must have
• I would like to have 2 pages that are similar, but have different questions on them so that every guest doesn't answer the same questions. On each page it needs to say 'Norah & Devin,' 'May 27th, 2011,' and a place that says 'Guest Names' for the guest sign their names.
Nice to have
• Some of the questions we like are:
Do you have any advice or wishes for the bride and groom?
How far did you travel to get here?
How do you know Norah and Devin?
What’s your favorite memory with the bride and groom?
What has been your favorite part of the wedding?
What do you think they'll name their children?
Should not have
• The pages do not need to be extremely colorful. An ivory or white background with accents of color would be preferred.

```html
<!DOCTYPE html>
<html lang="en">
<head>
<meta charset="utf-8">
<title>Norah + Devin — Guestbook Page</title>
<link rel="stylesheet" href="https://fonts.googleapis.com/css2?family=Caudex&display=swap">
<style>
  :root {
    --paper: #ffffff;
    --frame: #2b2b2b;
    --ink: #1f1f1f;
    --rule: #5b4fc0;
    --seal: #35288f;
    --seal-text: #ece56c;
    --lime: #8fe82a;
    --violet-deep: #2e1f8c;
    --violet-soft: #a99cf0;
    --mint: #eafbd8;
  }
  * { box-sizing: border-box; margin: 0; padding: 0; }
  html, body { width: 1200px; height: 900px; overflow: hidden; background: var(--paper); }
  body { position: relative; font-family: "Caudex", Georgia, serif; color: var(--ink); }

  .page {
    position: absolute; left: 168px; top: 17px; width: 864px; height: 865px;
    border: 1px solid var(--frame);
  }
  .artwork { position: absolute; left: 0; top: 0; width: 1200px; height: 900px; }

  .bouquet {
    position: absolute; width: 196px; height: 172px; border-radius: 46% 54% 50% 50%;
    background:
      radial-gradient(circle at 35% 40%, var(--mint) 0 12%, transparent 24%),
      radial-gradient(circle at 65% 62%, var(--violet-soft) 0 14%, transparent 28%),
      radial-gradient(circle at 50% 50%, var(--lime) 0 30%, var(--violet-deep) 62%, transparent 72%);
  }
  .bouquet--top-left { left: 185px; top: 35px; }
  .bouquet--top-right { left: 815px; top: 35px; }
  .bouquet--bottom-left { left: 188px; top: 697px; }
  .bouquet--bottom-right { left: 815px; top: 697px; }

  .seal {
    position: absolute; left: 513px; top: 43px; width: 170px; height: 170px;
    border-radius: 50%; background: var(--seal); color: var(--seal-text);
    text-align: center;
  }
  .seal__name { position: absolute; left: 0; right: 0; font-size: 22px; line-height: 1; }
  .seal__name--first { top: 33px; }
  .seal__plus { position: absolute; left: 0; right: 0; top: 57px; font-size: 15px; line-height: 1; }
  .seal__name--second { top: 72px; }
  .seal__date { position: absolute; left: 0; right: 0; top: 104px; font-size: 17px; line-height: 1; }

  .prompt { position: absolute; font-size: 16px; line-height: 20px; }
  .prompt--guests { left: 246px; top: 253px; }
  .prompt--favorite-part { left: 246px; top: 424px; width: 330px; }
  .prompt--memory { left: 600px; top: 424px; width: 345px; text-align: right; }
  .prompt--advice { left: 400px; top: 649px; width: 400px; text-align: center; }
</style>
</head>
<body>
  <div class="page"></div>

  <svg class="artwork" viewBox="0 0 1200 900" aria-hidden="true">
    <g class="ribbon" stroke="var(--lime)" fill="none">
      <line x1="300" y1="77" x2="900" y2="77" stroke-width="6"/>
      <line x1="300" y1="90" x2="900" y2="90" stroke-width="3"/>
      <line x1="300" y1="102" x2="900" y2="102" stroke-width="6"/>
      <line x1="300" y1="110" x2="900" y2="110" stroke-width="2"/>
      <line x1="300" y1="121" x2="900" y2="121" stroke-width="2" stroke-dasharray="14 10"/>
      <line x1="300" y1="133" x2="900" y2="133" stroke-width="6"/>
    </g>
    <g class="writing-lines" stroke="var(--rule)" stroke-width="1">
      <line x1="246" y1="275" x2="946" y2="275"/>
      <line x1="246" y1="308" x2="946" y2="308"/>
      <line x1="246" y1="341" x2="946" y2="341"/>
      <line x1="246" y1="374" x2="946" y2="374"/>

      <line x1="246" y1="465" x2="570" y2="465"/>
      <line x1="246" y1="498" x2="570" y2="498"/>
      <line x1="246" y1="531" x2="570" y2="531"/>
      <line x1="246" y1="564" x2="570" y2="564"/>
      <line x1="244" y1="597" x2="568" y2="597"/>

      <line x1="621" y1="465" x2="945" y2="465"/>
      <line x1="621" y1="498" x2="945" y2="498"/>
      <line x1="621" y1="531" x2="945" y2="531"/>
      <line x1="621" y1="564" x2="945" y2="564"/>
      <line x1="619" y1="597" x2="943" y2="597"/>

      <line x1="434" y1="689" x2="766" y2="689"/>
      <line x1="434" y1="722" x2="766" y2="722"/>
      <line x1="434" y1="755" x2="766" y2="755"/>
      <line x1="434" y1="788" x2="766" y2="788"/>
      <line x1="432" y1="821" x2="764" y2="821"/>
    </g>
  </svg>

  <div class="bouquet bouquet--top-left" role="img" aria-label="Cluster of purple and lime green flowers"></div>
  <div class="bouquet bouquet--top-right" role="img" aria-label="Cluster of purple and lime green flowers"></div>
  <div class="bouquet bouquet--bottom-left" role="img" aria-label="Cluster of purple and lime green flowers"></div>
  <div class="bouquet bouquet--bottom-right" role="img" aria-label="Cluster of purple and lime green flowers"></div>

  <header class="seal">
    <p class="seal__name seal__name--first">Norah</p>
    <p class="seal__plus">+</p>
    <p class="seal__name seal__name--second">Devin</p>
    <p class="seal__date">May 27th, 2011</p>
  </header>

  <p class="prompt prompt--guests">Guest names</p>
  <p class="prompt prompt--favorite-part">What has been your favorite part of<br>the wedding?</p>
  <p class="prompt prompt--memory">What’s your favorite memory with the<br>bride and groom?</p>
  <p class="prompt prompt--advice">Do you have any advice or wishes for<br>the bride and groom?</p>
</body>
</html>
```